Wine Label Design

We are looking for a new label to add to our winery. This is to be named "Feldkamm" which is the German word for schoolhouse. Our tasting room is a one room school house built in 1887. I would like the label to be very simple and clean with a schoolhouse on the front. I would like to schoolhouse to be sketch style, not a cartoonish design. I have attached a photo of the schoolhouse that we pour from, this is what I would want the schoolhouse to resemble. I have also added a copy of our current "higher end" label so that you have an idea of our style. I would like the new label to be cohesive with our old label and look good next to each other on our shelves. Just as added clarification we do not want Kolber Vineyards on the new label - we want that replaced with Feldkamm. If you are unable to do a full label design we would also accept just the schoolhouse drawing design as well. Thank you.

Feldkamm

```html
<!DOCTYPE html>
<html lang="en">
<head>
<meta charset="utf-8">
<title>Feldkamm — Wine Label Colourways</title>
<link rel="stylesheet" href="https://fonts.googleapis.com/css2?family=Cinzel:wght@400;500&family=Cormorant+Garamond:wght@500;600&family=Pinyon+Script&display=swap">
<style>
  :root {
    --page: #ffffff;
    --plum: #3a2034;
    --umber: #261d0e;
    --ink-light: #ffffff;
    --ink-soft: #d8c8d0;
    --ink-soft-umber: #d6ccc4;
    --art-paper: #e6e0d6;
    --art-tone: #8f8590;
    --art-dark: #2a2628;
  }
  * { margin: 0; padding: 0; box-sizing: border-box; }
  html, body {
    width: 1200px;
    height: 1000px;
    overflow: hidden;
    background: var(--page);
  }
  .canvas {
    position: relative;
    width: 1200px;
    height: 1000px;
  }
  .label {
    position: absolute;
    top: 198px;
    width: 483px;
    height: 604px;
    color: var(--ink-light);
    text-align: center;
  }
  .label--plum { left: 85px; background: var(--plum); --meta: var(--ink-soft); }
  .label--umber { left: 632px; background: var(--umber); --meta: var(--ink-soft-umber); }

  .label__brand {
    position: absolute;
    top: 78px;
    left: 0;
    width: 100%;
    font-family: "Cinzel", "Trajan Pro", serif;
    font-weight: 400;
    font-size: 52px;
    letter-spacing: 0.5px;
    line-height: 1;
  }
  .label__art {
    position: absolute;
    top: 159px;
    left: 148px;
    width: 187px;
    height: 196px;
    border: 2px solid #ffffff;
    background: linear-gradient(180deg, var(--art-paper) 0%, var(--art-tone) 55%, var(--art-dark) 100%);
  }
  .label__vintage {
    position: absolute;
    top: 408px;
    left: 0;
    width: 100%;
    font-family: "Cormorant Garamond", Georgia, serif;
    font-weight: 600;
    font-size: 19px;
    font-variant-numeric: lining-nums;
    letter-spacing: 5px;
    line-height: 1;
    color: var(--meta);
  }
  .label__varietal {
    position: absolute;
    top: 466px;
    left: 0;
    width: 100%;
    font-family: "Pinyon Script", cursive;
    font-size: 48px;
    line-height: 1.1;
  }
  .label__region {
    position: absolute;
    top: 552px;
    left: 0;
    width: 100%;
    font-family: "Cormorant Garamond", Georgia, serif;
    font-weight: 500;
    font-size: 17px;
    letter-spacing: 0.5px;
    color: var(--meta);
  }
</style>
</head>
<body>
  <main class="canvas">
    <section class="label label--plum">
      <h1 class="label__brand">FELDKAMM</h1>
      <div class="label__art" role="img" aria-label="Placeholder area for the schoolhouse illustration"></div>
      <p class="label__vintage">2017</p>
      <p class="label__varietal">Grenache</p>
      <p class="label__region">FINGER LAKES</p>
    </section>

    <section class="label label--umber">
      <h1 class="label__brand">FELDKAMM</h1>
      <div class="label__art" role="img" aria-label="Placeholder area for the schoolhouse illustration"></div>
      <p class="label__vintage">2017</p>
      <p class="label__varietal">Grenache</p>
      <p class="label__region">FINGER LAKES</p>
    </section>
  </main>
</body>
</html>
```